New professional looking flyer for company

I need our flyer updated my flyer is the Lvb flyer Have attached current flyer so you know what services need to be listed. Want it to be in mainly dark colours like black and dark grey with pops of light grey, silver or white. i have added several photos for you to choose which ones work best with your design would like The photos to be in colour for the flyer. But can have a mix of greyscale if that works for your design j have attached another companies flyers as design ideas to show what I am looking for

Target Market(s)

new clients

Industry/Entity Type

transport and earthmoving

Colors

Designer to choose colors to be used in the design.

Requirements
Nice to have
• Look professional
Should not have
• No orange or red or green

```html
<!DOCTYPE html>
<html lang="en">
<head>
<meta charset="utf-8">
<title>Lvb Pty Ltd – Our Services</title>
<link rel="stylesheet" href="https://fonts.googleapis.com/css2?family=Poppins:wght@400;500;600;700;800;900&display=swap">
<style>
  :root {
    --bg: #6f9fe6;
    --ink: #0b0b0c;
    --white: #ffffff;
    --silver: #c9cbce;
    --silver-dark: #8d9095;
    --gold: #e0a100;
    --muted: #b8b8b8;
  }
  * { box-sizing: border-box; margin: 0; padding: 0; }
  html, body { width: 1200px; height: 1027px; overflow: hidden; }
  body { background: var(--bg); font-family: "Poppins", sans-serif; position: relative; }

  .flyer {
    position: absolute; left: 260px; top: 33px; width: 680px; height: 961px;
    background: var(--ink); overflow: hidden; color: var(--white);
  }
  .corner { position: absolute; right: 0; top: 70px; width: 110px; height: 130px; }

  .hero {
    position: absolute; left: 40px; top: 55px; width: 600px; height: 300px;
    clip-path: polygon(0 0, 88% 0, 100% 14%, 100% 100%, 0 100%, 0 20%);
    background: linear-gradient(160deg, #3d4658 0%, #6b5a3c 45%, #3a3228 75%, #1d1c1b 100%);
  }
  .brand {
    position: absolute; left: 0; right: 0; top: 120px;
    display: flex; align-items: center; justify-content: center; gap: 10px;
  }
  .brand-mark { width: 14px; height: 14px; background: var(--white); border-radius: 50%; }
  .brand-name { font-size: 30px; font-weight: 700; letter-spacing: 1px; }
  .title {
    position: absolute; left: 0; right: 0; top: 160px; text-align: center;
    font-size: 78px; font-weight: 900; letter-spacing: 1px; line-height: 1;
    text-shadow: 0 3px 8px rgba(0,0,0,.5);
  }

  .gallery-frame {
    position: absolute; left: 48px; top: 262px; width: 584px; height: 132px;
    background: linear-gradient(90deg, var(--silver-dark), var(--white) 50%, var(--silver-dark));
  }
  .gallery { position: absolute; left: 58px; top: 270px; display: flex; gap: 10px; }
  .gallery .shot { width: 181px; height: 116px; }
  .shot-1 { background: linear-gradient(160deg, #4a6a98, #c9a06a 60%, #3b3b40); }
  .shot-2 { background: linear-gradient(170deg, #5d8fd6, #b7764c 60%, #8a4a2a); }
  .shot-3 { background: linear-gradient(170deg, #6f9ad8, #b98a3c 55%, #6b5a48); }

  .services {
    position: absolute; top: 418px; list-style: none;
    font-size: 14px; font-weight: 600; line-height: 26px;
  }
  .services-left { left: 50px; }
  .services-right { left: 380px; top: 440px; }
  .services li { display: flex; align-items: flex-start; gap: 8px; }
  .services li svg { flex: none; margin-top: 7px; }
  .services .two-line { line-height: 17px; padding: 5px 0; }
  .services .two-line svg { margin-top: 3px; }

  .pitch { position: absolute; left: 50px; top: 616px; width: 330px; }
  .pitch-lead { font-size: 14px; line-height: 20px; color: var(--muted); }
  .pitch-cta { font-size: 24px; font-weight: 900; line-height: 1.02; text-transform: uppercase; margin-top: 2px; }

  .truck {
    position: absolute; right: 0; top: 700px; width: 300px; height: 261px;
    background: linear-gradient(150deg, #6b5a22 0%, #2a2a2c 40%, #8b8e93 60%, #1a1a1c 100%);
  }

  .contact-band { position: absolute; left: 0; top: 730px; width: 420px; }
  .stripe { height: 6px; background: linear-gradient(90deg, var(--white), var(--silver) 60%, var(--silver-dark)); margin-bottom: 4px; }
  .stripe-gap { margin-top: 4px; }
  .contact { list-style: none; padding: 8px 0 8px 46px; background: linear-gradient(90deg, #e6e7e9, #a9acb1); color: var(--ink); }
  .contact li { display: flex; align-items: center; gap: 10px; font-size: 14px; font-weight: 700; line-height: 1.2; padding: 3px 0; }
  .contact svg { flex: none; }
</style>
</head>
<body>
  <main class="flyer">
    <svg class="corner" viewBox="0 0 110 130" aria-hidden="true"><polygon points="20,0 110,0 110,110" fill="var(--gold)"/></svg>

    <div class="hero" role="img" aria-label="Loader and road train working on a desert site at dusk"></div>
    <div class="brand"><span class="brand-mark"></span><span class="brand-name">Lvb Pty Ltd</span></div>
    <h1 class="title">OUR SERVICES</h1>

    <div class="gallery-frame"></div>
    <div class="gallery">
      <div class="shot shot-1" role="img" aria-label="White prime mover on an outback road at sunset"></div>
      <div class="shot shot-2" role="img" aria-label="Loader filling a tipper on red earth"></div>
      <div class="shot shot-3" role="img" aria-label="Crew beside a loader and water tanker"></div>
    </div>

    <ul class="services services-left">
      <li><svg width="12" height="12" viewBox="0 0 12 12"><circle cx="6" cy="6" r="5.5" fill="var(--gold)"/><path d="M3.3 6.2l1.8 1.8 3.6-3.8" stroke="#111" stroke-width="1.5" fill="none"/></svg>Over size loads / Hot Shot Load</li>
      <li><svg width="12" height="12" viewBox="0 0 12 12"><circle cx="6" cy="6" r="5.5" fill="var(--gold)"/><path d="M3.3 6.2l1.8 1.8 3.6-3.8" stroke="#111" stroke-width="1.5" fill="none"/></svg>Heavy Vehicle Recovery Services</li>
      <li><svg width="12" height="12" viewBox="0 0 12 12"><circle cx="6" cy="6" r="5.5" fill="var(--gold)"/><path d="M3.3 6.2l1.8 1.8 3.6-3.8" stroke="#111" stroke-width="1.5" fill="none"/></svg>Potable Water Deliveries</li>
      <li><svg width="12" height="12" viewBox="0 0 12 12"><circle cx="6" cy="6" r="5.5" fill="var(--gold)"/><path d="M3.3 6.2l1.8 1.8 3.6-3.8" stroke="#111" stroke-width="1.5" fill="none"/></svg>Road Building / Maintenance</li>
      <li><svg width="12" height="12" viewBox="0 0 12 12"><circle cx="6" cy="6" r="5.5" fill="var(--gold)"/><path d="M3.3 6.2l1.8 1.8 3.6-3.8" stroke="#111" stroke-width="1.5" fill="none"/></svg>Earthworks</li>
      <li><svg width="12" height="12" viewBox="0 0 12 12"><circle cx="6" cy="6" r="5.5" fill="var(--gold)"/><path d="M3.3 6.2l1.8 1.8 3.6-3.8" stroke="#111" stroke-width="1.5" fill="none"/></svg>Sand &amp; Metal Supply &amp; Cartage</li>
      <li><svg width="12" height="12" viewBox="0 0 12 12"><circle cx="6" cy="6" r="5.5" fill="var(--gold)"/><path d="M3.3 6.2l1.8 1.8 3.6-3.8" stroke="#111" stroke-width="1.5" fill="none"/></svg>Road Train Tippers</li>
    </ul>

    <ul class="services services-right">
      <li><svg width="12" height="12" viewBox="0 0 12 12"><circle cx="6" cy="6" r="5.5" fill="var(--gold)"/><path d="M3.3 6.2l1.8 1.8 3.6-3.8" stroke="#111" stroke-width="1.5" fill="none"/></svg>Road Train Tankers</li>
      <li><svg width="12" height="12" viewBox="0 0 12 12"><circle cx="6" cy="6" r="5.5" fill="var(--gold)"/><path d="M3.3 6.2l1.8 1.8 3.6-3.8" stroke="#111" stroke-width="1.5" fill="none"/></svg>Road Train Flat Tops</li>
      <li><svg width="12" height="12" viewBox="0 0 12 12"><circle cx="6" cy="6" r="5.5" fill="var(--gold)"/><path d="M3.3 6.2l1.8 1.8 3.6-3.8" stroke="#111" stroke-width="1.5" fill="none"/></svg>Drop Deck Trailers</li>
      <li class="two-line"><svg width="12" height="12" viewBox="0 0 12 12"><circle cx="6" cy="6" r="5.5" fill="var(--gold)"/><path d="M3.3 6.2l1.8 1.8 3.6-3.8" stroke="#111" stroke-width="1.5" fill="none"/></svg><span>Mine Site accredited equipment<br>&amp; Operators</span></li>
      <li><svg width="12" height="12" viewBox="0 0 12 12"><circle cx="6" cy="6" r="5.5" fill="var(--gold)"/><path d="M3.3 6.2l1.8 1.8 3.6-3.8" stroke="#111" stroke-width="1.5" fill="none"/></svg>Traffic Management</li>
    </ul>

    <div class="pitch">
      <p class="pitch-lead">We offer a large range services no</p>
      <p class="pitch-cta">Call us today for a<br>personalized quote<br>to suit your need.</p>
    </div>

    <div class="truck" role="img" aria-label="White road train prime mover hauling a loader on a low loader"></div>

    <div class="contact-band">
      <div class="stripe"></div>
      <ul class="contact">
        <li><svg width="16" height="12" viewBox="0 0 16 12"><rect x="0.5" y="0.5" width="15" height="11" rx="1.5" fill="var(--gold)"/><path d="M1 1.5l7 5 7-5" stroke="#111" stroke-width="1.3" fill="none"/></svg>info@lvbhaulage.com.au</li>
        <li><svg width="16" height="16" viewBox="0 0 16 16"><path d="M3 1.5l3 .5 1 3.5-1.8 1.3a9 9 0 0 0 4 4L10.5 9l3.5 1 .5 3-2 1.5C6.5 14 2 9.5 1.5 3.5z" fill="var(--gold)"/></svg>000 555 010</li>
        <li><svg width="16" height="20" viewBox="0 0 16 20"><path d="M8 0a7 7 0 0 1 7 7c0 5-7 13-7 13S1 12 1 7a7 7 0 0 1 7-7z" fill="var(--gold)"/><circle cx="8" cy="7" r="2.6" fill="#111"/></svg><span>Lvb Lot 41, Redgum Track<br>Marla Creek, Australia</span></li>
      </ul>
      <div class="stripe stripe-gap"></div>
      <div class="stripe"></div>
    </div>
  </main>
</body>
</html>
```